Präsentationsvorlagen für virtuelles Vertriebstraining
Zielgruppe
Ich biete virtuelles Vertriebstraining an. Das heißt ich bringe Vetriebsmannschaften bei, wie sie Videos und Online Collaboration Tools nutzen können um besser zu verkaufen.
Zielgruppe sind Firmen, die anspruchsvolle, erklärungsbedürftige Produkte im B2B Umfeld vertrieben.
Aufgabenstellung
In meinen Präsentationen arbeite ich mit relativ wenig Text und vielen Bildern.
Das Design soll sehr futuristisch und modern sein, wobei ein gewisser 80er Cyberpunk Stil durchaus willkommen ist.
Nicht zu verspielt sehr, klar. Anthrazit, Metall mit Neon Elementen.
Powerpoint Format

```html
<!DOCTYPE html>
<html lang="de">
<head>
<meta charset="utf-8">
<title>Typoblindtext – Präsentationsfolie</title>
<link rel="stylesheet" href="https://fonts.googleapis.com/css2?family=Montserrat:wght@300;400;500;700&display=swap">
<style>
  :root {
    --neon-pink: #f93bd6;
    --neon-blue: #6475ff;
    --neon-cyan: #99ffff;
    --steel-grey: #d6d5de;
    --anthracite: #2c3134;
    --paper: #ffffff;
    --ink: #111111;
  }
  * { margin: 0; padding: 0; box-sizing: border-box; }
  html, body {
    width: 1200px;
    height: 849px;
    overflow: hidden;
    background: var(--paper);
    font-family: "Montserrat", sans-serif;
  }
  .slide {
    position: absolute;
    left: 63px;
    top: 45px;
    width: 1075px;
    height: 761px;
    background: var(--paper);
    box-shadow: 4px 5px 7px rgba(0, 0, 0, 0.35);
    overflow: hidden;
  }
  .header-bands {
    position: absolute;
    left: 0;
    top: 0;
    width: 1075px;
    height: 81px;
  }
  .slide-title {
    position: absolute;
    left: 561px;
    top: 20px;
    font-size: 40px;
    line-height: 44px;
    font-weight: 300;
    letter-spacing: 1px;
    color: var(--paper);
  }
  .brand {
    position: absolute;
    left: 910px;
    top: 15px;
    display: flex;
    align-items: center;
    height: 54px;
  }
  .brand-name {
    font-size: 14px;
    line-height: 17.5px;
    font-weight: 300;
    color: var(--paper);
    text-transform: uppercase;
    padding-right: 9px;
    border-right: 1px solid var(--paper);
  }
  .brand-square {
    width: 44px;
    height: 44px;
    margin-left: 16px;
    background: var(--paper);
  }
  .pie-chart {
    position: absolute;
    left: 112px;
    top: 221px;
    width: 322px;
    height: 322px;
  }
  .key-figure {
    position: absolute;
    left: 490px;
    top: 212px;
    font-size: 73px;
    line-height: 80px;
    font-weight: 700;
    color: var(--ink);
  }
  .body-copy {
    position: absolute;
    left: 493px;
    width: 470px;
    font-size: 14.4px;
    line-height: 19.2px;
    text-align: justify;
    letter-spacing: 0.35px;
    color: var(--ink);
  }
  .body-copy.intro { top: 294px; font-weight: 400; }
  .body-copy.intro strong { font-weight: 500; }
  .body-copy.summary { top: 463px; font-weight: 500; }
  .footer-band {
    position: absolute;
    left: 0;
    bottom: 0;
    width: 100%;
    height: 22px;
    background: var(--neon-blue);
  }
</style>
</head>
<body>
  <main class="slide">
    <svg class="header-bands" viewBox="0 0 1075 81" aria-hidden="true">
      <polygon points="0,0 354,0 390,41 0,41" fill="var(--neon-pink)"/>
      <polygon points="393,0 1075,0 1075,81 464,81" fill="var(--anthracite)"/>
    </svg>
    <h1 class="slide-title">TYPOBLINDTEXT</h1>
    <div class="brand">
      <p class="brand-name">Kanzo<br>Vertriebs<br>akademie</p>
      <span class="brand-square"></span>
    </div>

    <svg class="pie-chart" viewBox="0 0 322 322" role="img" aria-label="Kreisdiagramm mit vier Anteilen">
      <path d="M161,161 L161,0 A161,161 0 1 1 107,313 Z" fill="var(--neon-pink)"/>
      <path d="M161,161 L107,313 A161,161 0 0 1 2,134 Z" fill="var(--neon-blue)"/>
      <path d="M161,161 L2,134 A161,161 0 0 1 58,37 Z" fill="var(--neon-cyan)"/>
      <path d="M161,161 L58,37 A161,161 0 0 1 161,0 Z" fill="var(--steel-grey)"/>
    </svg>

    <p class="key-figure">65%</p>
    <p class="body-copy intro"><strong>Dies ist ein Typoblindtext.</strong> An ihm kann man sehen, ob alle Buchstaben da sind und wie sie aussehen. Manchmal benutzt man Worte wie Hamburgefonts, Rafgenduks oder Handgloves, um Schriften zu testen. Manchmal Sätze, die alle Buchstaben des Alphabets enthalten - man nennt diese Sätze »Pangrams«. Sehr bekannt ist dieser: The quick brown fox jumps over the lazy old dog. Oft werden in Typoblindtexte auch fremdsprachige Worte benutzt.</p>
    <p class="body-copy summary">Dies ist ein Typoblindtext. An ihm kann man sehen, ob alle Buchstaben da sind und wie sie aussehen. Manchmal benutzt man Worte wie Hamburgefonts, Rafgenduks oder Handgloves, um Schriften zu testen.</p>

    <div class="footer-band"></div>
  </main>
</body>
</html>
```